Bookcover: Lessons From the Silent Orchard

I am publishing a super-low-cost innovation book for €4,99 on Bravolo Self Release to help everyone become a great innovator: young ambitious people without college education nor a big budget. Do you want to help me?

Brief:
Design a book cover 1600 x 2560 pixels for BSR.
Main title: Lessons From the Silent Orchard
Sub title: Roots - Patience - Growth & Harvest
Author: Maarten de Klerk
Design: captive, and appealing to everyone
Target Group: young ambitious people without college education

For bravolo please format the height/width ratio of 1.6:1

```html
<!DOCTYPE html>
<html lang="en">
<head>
<meta charset="utf-8">
<title>Lessons From the Silent Orchard — Book Cover</title>
<link rel="stylesheet" href="https://fonts.googleapis.com/css2?family=Lato:wght@300;900&family=Ubuntu:wght@500&family=Roboto:ital,wght@1,300&display=swap">
<style>
  :root {
    --backdrop: #fecf86;
    --paper: #fcf0da;
    --ink: #461d13;
    --orange: #f39a2c;
    --yellow: #fdd262;
    --sand: #e2d3bb;
  }
  * { margin: 0; padding: 0; box-sizing: border-box; }
  html, body {
    width: 1200px;
    height: 1200px;
    overflow: hidden;
    background: var(--backdrop);
  }
  .cover {
    position: absolute;
    left: 250px;
    top: 40px;
    width: 700px;
    height: 1120px;
    background: var(--paper);
    color: var(--ink);
    text-align: center;
  }
  .title-lead,
  .title-main,
  .subtitle,
  .author {
    position: absolute;
    left: 0;
    right: 0;
    white-space: nowrap;
  }
  .title-lead {
    top: 96px;
    font: 300 48px/1 "Lato", sans-serif;
    letter-spacing: -0.5px;
  }
  .title-main {
    font-family: "Lato", sans-serif;
    font-weight: 900;
    line-height: 1;
  }
  .title-main.first {
    top: 148px;
    font-size: 120px;
    letter-spacing: 6px;
  }
  .title-main.second {
    top: 268px;
    font-size: 100px;
    letter-spacing: 0;
  }
  .subtitle {
    top: 378px;
    font: 500 32px/1 "Ubuntu", sans-serif;
  }
  .illustration {
    position: absolute;
    left: 90px;
    top: 424px;
    width: 523px;
    height: 584px;
    border-radius: 50% 50% 12px 12px;
    background: radial-gradient(circle at 50% 40%, var(--yellow) 0%, var(--orange) 45%, var(--sand) 75%, var(--paper) 100%);
  }
  .author {
    top: 1018px;
    font: italic 300 48px/1 "Roboto", sans-serif;
  }
</style>
</head>
<body>
  <main class="cover">
    <h1 class="title">
      <span class="title-lead">LESSONS FROM THE</span>
      <span class="title-main first">SILENT</span>
      <span class="title-main second">ORCHARD</span>
    </h1>
    <p class="subtitle">Roots - Patience - Growth &amp; Harvest</p>
    <div class="illustration" role="img" aria-label="Flat illustration of a head in profile with a glowing light bulb in the mind, a gear, a target and a map pin on a round beige backdrop"></div>
    <p class="author">Maarten de Klerk</p>
  </main>
</body>
</html>
```